Webdesign for Property Renting Business

We need a professional and slim design for a hight quality property renting website which is not overcrowded with too much information and has a clear and easily structure to read. The visitor should get an instant impression what he can do at a glance.

The goal of this contest is to get a design for building a prototype of the website and to attract our client and owner of the site by a good looking prototype and not just a wireframe. Therefore we don't need an HTML-coded design at this early project-stage. We only expect getting a simple bitmap or vector-graphic design.

Actually we don't have a logo. Use a placeholder or feel free to design a simple one by yourself.

Last but not least if you have a good idea just include it in to your design.

Our goal is to get a design for building a prototype of the website and to attract our client by a good looking prototype and not just a wireframe.

Target Market(s)

People who want to spend money to rent a good quality property. Not only the riches. These could be business people and also demanding families as well.

Industry/Entity Type

Building

Colors
85cae6

Requirements
Must have
• We need two sites, a start site and a property-details site. Each site has to include the following points:

1.) start site
- search mask (location, date to choose, quanity of guests)
- show some properties (highlights, special offers etc.)
- show login/register link

2.) property site
- Location in Vorlen Map
- Photos, Description, Amenities, Calendar (available,not available), Contact, Reviews

These are some sites which I like from a design prospective
- http://www.stayquelo.com
- http://www.lodvanta.com/
- http://www.dwellirox.com/
- http://www.plomavi.com

These are some sites which I dislike:
1.) http://www.gallic-estatio.com/guides/france/rent/
2.) http://www.solohomvenu.co.za/property-rentals.htm

We don't need an HTML-coded design at this early project-stage. We only expect getting a simple bitmap or vector-graphic design. Maybe with the PSD-file (or wathever program you use) that we can pick-out some elements for building the prototype.

```html
<!DOCTYPE html>
<html lang="en">
<head>
<meta charset="utf-8">
<title>Roomvale – Find your property</title>
<link href="https://fonts.googleapis.com/css2?family=Open+Sans:wght@400;600;700&family=Roboto+Slab:wght@300;400;700&display=block" rel="stylesheet">
<style>
:root{
  --nav-bg:#262c33;
  --hero-dark:#3c4248;
  --hero-mid:#5b6167;
  --hero-light:#7d8388;
  --cyan:#19d3e0;
  --cyan-deep:#00c2d0;
  --blue:#1a5fc7;
  --white:#ffffff;
  --text:#4a4a4a;
  --heading:#2b2b2b;
  --field-label:#4b4b4b;
  --band:#f3f4f4;
  --slab:"Roboto Slab","Rockwell","Roboto Serif",serif;
}
*{box-sizing:border-box;margin:0;padding:0}
html,body{width:1200px;height:1000px;overflow:hidden;background:var(--white)}
body{position:relative;font-family:"Open Sans",Arial,sans-serif;color:var(--text)}

.site-header{position:absolute;left:0;top:0;width:1200px;height:61px;background:var(--nav-bg);z-index:2}
.brand{position:absolute;left:112px;top:14px;display:flex;align-items:center;gap:10px;color:var(--white);font-family:var(--slab);font-weight:400;font-size:24px;line-height:32px}
.brand-dot{width:32px;height:32px;border-radius:50%;background:var(--cyan)}
.main-nav{position:absolute;left:495px;top:22px;display:flex;gap:25px}
.main-nav a{color:var(--white);text-decoration:none;font-weight:700;font-size:11.5px;line-height:16px}
.btn{position:absolute;top:13px;height:35px;border-radius:3px;font-weight:700;font-size:11.5px;display:flex;align-items:center;justify-content:center;text-decoration:none}
.btn-register{left:928px;width:80px;background:linear-gradient(#fff,#e9e9e9);color:#2b2b2b}
.btn-login{left:1022px;width:67px;background:var(--blue);color:var(--white)}

.hero{position:absolute;left:0;top:61px;width:1200px;height:410px;overflow:hidden}
.hero-photo{position:absolute;inset:0;background:linear-gradient(100deg,var(--hero-dark) 0%,var(--hero-mid) 45%,var(--hero-light) 75%,var(--hero-mid) 100%)}
.hero-photo::after{content:"";position:absolute;inset:0;background:linear-gradient(180deg,rgba(30,34,38,.35),rgba(30,34,38,.1) 60%,rgba(30,34,38,.25))}
.hero-title{position:absolute;left:112px;top:108px;font-family:var(--slab);font-weight:700;font-size:50px;line-height:66px;color:var(--white);text-shadow:0 2px 4px rgba(0,0,0,.35)}
.search-panel{position:absolute;left:112px;top:194px;width:671px;height:61px;background:rgba(38,44,51,.8);border-radius:3px}
.field{position:absolute;top:11px;height:36px;background:var(--white);border-radius:3px;display:flex;align-items:center;justify-content:space-between;padding:0 9px;font-weight:600;font-size:12.5px;color:var(--field-label)}
.field svg{flex:none}
.field-where{left:11px;width:226px}
.field-in{left:250px;width:114px}
.field-out{left:377px;width:114px}
.field-guests{left:505px;width:149px}
.search-btn{position:absolute;left:795px;top:193px;width:225px;height:61px;border:0;border-radius:3px;background:linear-gradient(var(--cyan) 50%,var(--cyan-deep) 50%);box-shadow:0 2px 3px rgba(0,0,0,.3);display:flex;align-items:center;justify-content:center;gap:12px;color:var(--white);font-family:var(--slab);font-weight:700;font-size:27px;letter-spacing:.5px}
.hero-arrow{position:absolute;top:193px}
.hero-arrow.prev{left:18px}
.hero-arrow.next{left:1148px}

.welcome{position:absolute;left:0;top:471px;width:1200px;text-align:center}
.welcome h1{position:absolute;left:0;top:42px;width:1200px;font-family:var(--slab);font-weight:300;font-size:32px;line-height:42px;color:var(--heading)}
.welcome .rule{position:absolute;left:574px;top:90px;width:54px;height:2px;background:var(--cyan)}
.welcome .intro{position:absolute;left:125px;top:102px;width:950px;font-size:15.5px;line-height:24px;color:#555}

.feature{position:absolute;top:660px;width:300px;text-align:center}
.feature svg{display:block;margin:0 auto}
.feature h2{margin-top:18px;font-family:var(--slab);font-weight:300;font-size:21px;line-height:30px;color:var(--heading)}
.feature p{margin-top:20px;font-size:12.5px;line-height:22px;color:var(--text)}
.f1{left:116px}.f2{left:453px}.f3{left:784px}

.bottom-band{position:absolute;left:0;top:975px;width:1200px;height:25px;background:var(--band)}
</style>
</head>
<body>

<header class="site-header">
  <a class="brand"><span class="brand-dot"></span>Roomvale</a>
  <nav class="main-nav">
    <a>SEARCH</a><a>LISTINGS</a><a>ADVERTISE</a><a>ABOUT US</a><a>CONTACT US</a>
  </nav>
  <a class="btn btn-register">REGISTER</a>
  <a class="btn btn-login">LOGIN</a>
</header>

<section class="hero">
  <div class="hero-photo" role="img" aria-label="Photo of a modern grey living room with sofa and cushions"></div>
  <svg class="hero-arrow prev" width="30" height="46" viewBox="0 0 30 46"><path d="M24 4 L8 23 L24 42" fill="none" stroke="rgba(255,255,255,.55)" stroke-width="6"/></svg>
  <svg class="hero-arrow next" width="30" height="46" viewBox="0 0 30 46"><path d="M6 4 L22 23 L6 42" fill="none" stroke="rgba(255,255,255,.55)" stroke-width="6"/></svg>
  <h1 class="hero-title">Find your property.</h1>
  <form class="search-panel">
    <div class="field field-where">Where do you want to stay?
      <svg width="10" height="14" viewBox="0 0 10 14"><path d="M5 0a5 5 0 0 1 5 5c0 3.5-5 9-5 9S0 8.5 0 5a5 5 0 0 1 5-5z" fill="#19d3e0"/><circle cx="5" cy="5" r="1.8" fill="#fff"/></svg></div>
    <div class="field field-in">Check In
      <svg width="18" height="14" viewBox="0 0 18 14"><rect x="1" y="2" width="14" height="11" rx="1" fill="#19d3e0"/><rect x="3" y="6" width="10" height="5" fill="#fff"/><rect x="4" y="0" width="2" height="4" fill="#19d3e0"/><rect x="10" y="0" width="2" height="4" fill="#19d3e0"/><path d="M13 7h4m-2-2 2 2-2 2" stroke="#19d3e0" stroke-width="1.5" fill="none"/></svg></div>
    <div class="field field-out">Check Out
      <svg width="18" height="14" viewBox="0 0 18 14"><rect x="1" y="2" width="14" height="11" rx="1" fill="#19d3e0"/><rect x="3" y="6" width="10" height="5" fill="#fff"/><rect x="4" y="0" width="2" height="4" fill="#19d3e0"/><rect x="10" y="0" width="2" height="4" fill="#19d3e0"/><path d="M13 7h4m-2-2 2 2-2 2" stroke="#19d3e0" stroke-width="1.5" fill="none"/></svg></div>
    <div class="field field-guests">No. of Guests
      <svg width="16" height="13" viewBox="0 0 16 13"><circle cx="5" cy="3.5" r="3" fill="#19d3e0"/><path d="M0 13c0-4 2-6 5-6s5 2 5 6z" fill="#19d3e0"/><circle cx="11" cy="3" r="2.6" fill="#19d3e0"/><path d="M9 7c1-.6 4-.6 5 .5s2 3 2 5.5h-5c0-2.5-.5-4.5-2-6z" fill="#19d3e0"/></svg></div>
  </form>
  <button class="search-btn" type="button">SEARCH
    <svg width="24" height="24" viewBox="0 0 24 24"><circle cx="10" cy="10" r="7" fill="none" stroke="#fff" stroke-width="3.5"/><path d="M15 15l7 7" stroke="#fff" stroke-width="4.5" stroke-linecap="round"/></svg>
  </button>
</section>

<section class="welcome">
  <h1>Welcome to Roomvale</h1>
  <span class="rule"></span>
  <p class="intro">Lorem ipsum dolor sit amet, consectetur adipiscing elit. Proin sit amet sagittis erat. Maecenas suscipit ut quam id condimentum. Pellentesque cursus lacinia sapien et laoreet. Ut mattis ultricies sem id elementum. Vestibulum blandit consectetur nibh.</p>
</section>

<article class="feature f1">
  <svg width="118" height="134" viewBox="0 0 118 134">
    <defs><clipPath id="c1"><circle cx="59" cy="59" r="58"/></clipPath></defs>
    <path d="M47 112 L59 134 L71 112z" fill="#00c2d0"/>
    <circle cx="59" cy="59" r="58" fill="#00c2d0"/>
    <rect x="0" y="0" width="118" height="61" fill="#19d3e0" clip-path="url(#c1)"/>
    <path d="M42 36h34v10c0 12-7 20-17 20s-17-8-17-20z" fill="#fff"/>
    <path d="M42 40h-9c0 10 5 15 12 16M76 40h9c0 10-5 15-12 16" fill="none" stroke="#fff" stroke-width="4"/>
    <rect x="55" y="64" width="8" height="12" fill="#fff"/>
    <ellipse cx="59" cy="82" rx="14" ry="5" fill="#fff"/>
  </svg>
  <h2>Easy and Effortless</h2>
  <p>Aenean sollicitudin, lorem quis bibendum auctor, nisi elit consequat ipsum, nec sagittis sem nibh id elit. Duis sed odio sit amet nibh vulputate cursus</p>
</article>

<article class="feature f2">
  <svg width="118" height="134" viewBox="0 0 118 134">
    <defs><clipPath id="c2"><circle cx="59" cy="59" r="58"/></clipPath></defs>
    <path d="M47 112 L59 134 L71 112z" fill="#00c2d0"/>
    <circle cx="59" cy="59" r="58" fill="#00c2d0"/>
    <rect x="0" y="0" width="118" height="61" fill="#19d3e0" clip-path="url(#c2)"/>
    <rect x="34" y="48" width="10" height="34" rx="3" fill="#fff"/>
    <path d="M48 50 L60 32 c3-5 9-3 8 3 l-3 11 h12 c5 0 7 4 6 8 l-5 22 c-1 4-4 6-8 6 H48z" fill="#fff"/>
  </svg>
  <h2>Trusted &amp; Reliable</h2>
  <p>Aenean sollicitudin, lorem quis bibendum auctor, nisi elit consequat ipsum, nec sagittis sem nibh id elit. Duis sed odio sit amet nibh vulputate cursus</p>
</article>

<article class="feature f3">
  <svg width="118" height="134" viewBox="0 0 118 134">
    <defs><clipPath id="c3"><circle cx="59" cy="59" r="58"/></clipPath></defs>
    <path d="M47 112 L59 134 L71 112z" fill="#00c2d0"/>
    <circle cx="59" cy="59" r="58" fill="#00c2d0"/>
    <rect x="0" y="0" width="118" height="61" fill="#19d3e0" clip-path="url(#c3)"/>
    <path d="M32 68 L58 44 L72 44 L74 58 L48 84z" fill="#fff"/>
    <circle cx="67" cy="51" r="3" fill="#00c2d0"/>
    <path d="M67 51c4-6 8-12 14-14 5-1 5 5 1 8" fill="none" stroke="#fff" stroke-width="2.5"/>
  </svg>
  <h2>Affordable</h2>
  <p>Aenean sollicitudin, lorem quis bibendum auctor, nisi elit consequat ipsum, nec sagittis sem nibh id elit. Duis sed odio sit amet nibh vulputate cursus</p>
</article>

<div class="bottom-band"></div>

</body>
</html>
```